Motorcycle Shop Business Card

New business card for Motorcycle repair and customization shop.Business name: Copper Falcon Chris Morris443-865-5190, 7214 Quarry Lane Halvern, MD 21990. www.dale@copperfalconcustoms.example. I uploaded some motorcycle images and logo and a couple of our calendar shoots. They do not have to be used on card just examples of some of our work and past graphic work.
We work on Vantor Brennick and Custom Built Motorcycles.

Looking for front and back design

Target Market(s)

Motorcycle owners

Industry/Entity Type

Motorcycle Part

```html
<!DOCTYPE html>
<html lang="en">
<head>
<meta charset="utf-8">
<title>Copper Falcon Customs – Business Cards</title>
<link href="https://fonts.googleapis.com/css2?family=Roboto:wght@400;700&display=swap" rel="stylesheet">
<style>
  :root {
    --page: #ececec;
    --sky: #a3dce6;
    --ink: #1f1f22;
    --iron-dark: #1c1d20;
    --iron-rust: #3a2a22;
    --text-light: #f2f2f2;
    --text-soft: #dcdcdc;
  }
  * { margin: 0; padding: 0; box-sizing: border-box; }
  html, body {
    width: 1200px; height: 800px; overflow: hidden;
    background: var(--page);
    font-family: "Roboto", Arial, sans-serif;
  }
  .stage { position: relative; width: 1200px; height: 800px; }
  .card {
    position: absolute; top: 245px;
    width: 540px; height: 310px;
    overflow: hidden; border-radius: 2px;
    box-shadow: 0 2px 6px rgba(0,0,0,0.18);
    background: var(--sky);
  }
  .card--back { left: 40px; }
  .card--front { left: 620px; }
  .card-art { position: absolute; inset: 0; width: 100%; height: 100%; }
  .wordmark {
    position: absolute;
    color: var(--ink);
    font-weight: 400;
    line-height: 1.1;
    text-align: center;
    letter-spacing: 0.3px;
    white-space: nowrap;
  }
  .card--back .wordmark { left: 0; right: 0; top: 122px; font-size: 28px; }
  .card--front .wordmark { left: 10px; width: 185px; top: 128px; font-size: 23px; }
  .contact {
    position: absolute; left: 250px; top: 70px; width: 280px;
    color: var(--text-light);
  }
  .contact-name {
    font-weight: 700; font-size: 20px; line-height: 1.25;
    margin-bottom: 16px;
  }
  .contact-list {
    list-style: none; text-align: center;
    font-size: 13px; line-height: 1.45; color: var(--text-soft);
    white-space: nowrap;
  }
</style>
</head>
<body>
<main class="stage">

  <section class="card card--back" aria-label="Business card back">
    <svg class="card-art" viewBox="0 0 540 310" preserveAspectRatio="none">
      <defs>
        <linearGradient id="ironBack" x1="0" y1="0" x2="1" y2="1">
          <stop offset="0" stop-color="var(--iron-dark)"/>
          <stop offset="0.55" stop-color="var(--iron-rust)"/>
          <stop offset="1" stop-color="var(--iron-dark)"/>
        </linearGradient>
      </defs>
      <g role="img" aria-label="Dark weathered metal texture with glowing sparks">
        <path d="M0 0 H540 V40 C430 40 350 95 250 105 C150 115 70 80 0 75 Z" fill="url(#ironBack)"/>
        <path d="M0 255 C120 230 260 235 380 255 C450 266 500 272 540 270 V310 H0 Z" fill="url(#ironBack)"/>
      </g>
    </svg>
    <p class="wordmark">Copper Falcon<br>Customs</p>
  </section>

  <section class="card card--front" aria-label="Business card front">
    <svg class="card-art" viewBox="0 0 540 310" preserveAspectRatio="none">
      <defs>
        <linearGradient id="ironFront" x1="0" y1="0" x2="1" y2="1">
          <stop offset="0" stop-color="var(--iron-rust)"/>
          <stop offset="0.5" stop-color="var(--iron-dark)"/>
          <stop offset="1" stop-color="var(--iron-rust)"/>
        </linearGradient>
      </defs>
      <path role="img" aria-label="Dark weathered metal texture with glowing sparks"
            d="M235 0 H540 V310 H235 L228 240 L210 232 C196 190 196 120 212 80 L230 74 Z"
            fill="url(#ironFront)"/>
    </svg>
    <p class="wordmark">Copper Falcon<br>Customs</p>
    <div class="contact">
      <p class="contact-name">Copper Falcon<br>Dale Fenwick</p>
      <ul class="contact-list">
        <li>Phone:-</li>
        <li>410-555-0137, 7214</li>
        <li>Website:-</li>
        <li>www.dale@copperfalconcustoms.example</li>
        <li>Location:-</li>
        <li>Quarry Lane Halvern, MD 21990 .</li>
      </ul>
    </div>
  </section>

</main>
</body>
</html>
```